ONE PAGE WEB DESIGN NEEDED for Finance Company

We need a web design (ONE PAGE DESIGN ONLY) for a new finance website called Corvella Lending. Corvella Lending helps customers get the right loan, whether its a home loan, investment loan, business loan etc.

You are required to come up with just the homepage design. Professionalism and quality is the key factors in the successful design.

Here are a few design questions to help you out:

-
What information should be used on the page?
Ive provided a document which outlines all the information needed to put on homepage (attached to the brief - called corvella_page_info). Also see the Must Have section below on this brief.

-
What links should appear in the navigation/footer?:
The navigation should provide links to the following pages (NOTE: services link has subcategories):
1 Homepage
2 Services
- Home loans
- Investment loans
- Refinancing loans
- Business loans
3 About Us
4 FAQ
5 Contact Us

-
What colors should be used in the design?
Our company colors - Cyan: #2EADE3, Blue: #004B70, White. Feel free to submit designs with slight variations if you feel it improves the design.

-
What should the layout of the page be?
This is up to you to come up with - we are open to different layouts for the page design (as long as they capture the information effectively and making it easy to understand).

Target Market(s)

Potential Home owners, Families and Business Owners

Industry/Entity Type

Business

Requirements
Must have
• - Must contain our logo (attached as PNG and Illustrator file)
- Winning designer must supply a Photoshop file (PSD) that will allow us.
Nice to have
• - Should include photos/images of families, professional groups, tradespeople etc (you can use stock photos from PixelVaultImages and I will purchase them once you are selected as the winning design)
- Link to a loan calculator somewhere on front page with a button 'Find out how much you could borrow' (or maybe even try adding a loan calculator to the homepage if you think this would look good)
- Page should have a main headline "Finding the right loan for you" or "Corvella Lending finds the right loan for our customers."
- Must include Accreditation logos somewhere on the homepage (will try and supply these soon)
Should not have
• - Poor quality designs will not be considered
- Do not use clipart

```html
<!DOCTYPE html>
<html lang="en">
<head>
<meta charset="utf-8">
<title>Corvella Lending – Finding the right loan for you</title>
<link href="https://fonts.googleapis.com/css2?family=Varela+Round&family=Arimo:wght@400;700&display=swap" rel="stylesheet">
<style>
:root{
  --cyan:#2eade3;
  --cyan-dark:#1c95c9;
  --slate:#55596a;
  --slate-dark:#4a4e5e;
  --panel:#f4f4f5;
  --page-grey:#ebebeb;
  --text:#55596a;
  --muted:#8a8d98;
  --white:#ffffff;
  --rule:#e3e3e5;
}
*{margin:0;padding:0;box-sizing:border-box}
html,body{width:1200px;height:903px;overflow:hidden;background:var(--white)}
body{position:relative;font-family:"Arimo",Arial,sans-serif;color:var(--text)}
.abs{position:absolute}

/* header */
.header-band{left:0;top:0;width:1200px;height:58px;background:var(--page-grey);border-top:2px solid #cfcfd2}
.account-links{right:200px;top:0;display:flex;gap:2px}
.account-links span{background:#b9bbc2;color:var(--white);font-size:8px;font-weight:700;padding:2px 6px 2px}
.logo{left:200px;top:16px;display:flex;align-items:center;gap:7px}
.logo-mark{width:30px;height:30px;border-radius:50%;border:3px solid var(--cyan)}
.logo-name{font-family:"Varela Round",sans-serif;font-size:26px;color:var(--cyan);letter-spacing:-.5px}
.advice{left:542px;top:20px;display:flex;align-items:flex-end;gap:3px}
.advice small{position:absolute;left:21px;top:0;font-size:10px;color:#a9abb3;font-family:"Varela Round",sans-serif}
.advice strong{font-family:"Arimo",sans-serif;font-weight:400;font-size:21px;color:var(--slate);margin-top:9px;letter-spacing:-.5px}
.util-links{right:200px;top:44px;font-size:10px;font-weight:700;color:var(--slate);letter-spacing:.3px}

/* nav */
.nav-band{left:0;top:58px;width:1200px;height:31px;background:var(--slate)}
.main-nav{left:199px;top:58px;display:flex;height:31px;width:555px}
.main-nav a{background:var(--cyan);color:var(--white);text-decoration:none;font-family:"Varela Round",sans-serif;font-size:13px;display:flex;align-items:center;justify-content:center;white-space:nowrap;border-right:1px solid #7fcdef;letter-spacing:.3px}
.main-nav a:last-child{border-right:0}
.nav-services{width:75px}
.nav-home{width:99px}
.nav-invest{width:132px}
.nav-refi{width:136px}
.nav-business{width:113px}
.search{left:762px;top:62px;width:238px;height:23px;background:var(--white);font-size:9px;color:#b5b7bd;padding:6px 6px}
.search svg{position:absolute;right:6px;top:5px}

/* hero area */
.hero-band{left:0;top:89px;width:1200px;height:309px;background:var(--page-grey)}
.hero{left:199px;top:98px;width:555px;height:292px;background:linear-gradient(120deg,#f6f5f2 0%,#e8e2d6 30%,#cbb39a 55%,#8fa271 85%,#5e7445 100%)}
.hero-title{left:211px;top:108px;font-family:"Varela Round",sans-serif;font-size:17px;color:var(--slate)}
.hero-link{left:212px;top:127px;font-size:8px;color:var(--cyan)}
.dots{left:697px;top:371px;display:flex;gap:4px}
.dots i{width:10px;height:10px;border-radius:50%;background:var(--white);border:2px solid #9aa0aa}
.dots i.on{border-color:var(--cyan);background:var(--cyan);box-shadow:inset 0 0 0 2px var(--white)}

/* calculator */
.calc{left:762px;top:98px;width:238px;height:167px;background:var(--panel)}
.calc-head{left:762px;top:98px;width:238px;height:20px;background:var(--slate);color:var(--white);font-family:"Varela Round",sans-serif;font-size:11px;padding:5px 6px}
.calc-row{font-family:"Varela Round",sans-serif;font-size:11px;color:var(--slate)}
.field{border:1px solid #cfd0d4;background:#f9f9f9;color:#9a9ca5;font-size:10px;padding:2px 4px;display:inline-block}
.track{height:7px;border-radius:4px;background:#e0e1e4;border:1px solid #cdd0d6}
.fill{height:100%;border-radius:4px;background:linear-gradient(var(--cyan),var(--cyan-dark))}
.knob{width:14px;height:14px;border-radius:50%;background:var(--white);border:2px solid var(--cyan);top:-5px}
.ticks{display:flex;gap:2px;font-size:7px;color:var(--slate)}
.ticks span{background:#bfe3f3;text-align:center;padding:1px 0}
.ticks span.blank{background:transparent}
.repay{left:762px;top:265px;width:115px;height:125px;background:var(--cyan);color:var(--white);padding:7px 7px;font-family:"Varela Round",sans-serif}
.repay h3{font-size:11px;font-weight:400;margin-bottom:13px}
.repay p{font-size:9px;line-height:9px}
.repay b{font-size:15px;font-weight:400;display:block;line-height:16px;margin-bottom:2px}
.apply{left:878px;top:265px;width:122px;height:125px;background:var(--slate);color:var(--white);padding:7px 11px;font-family:"Varela Round",sans-serif}
.apply h3{font-size:11px;font-weight:400;margin-bottom:12px}
.apply li{list-style:none;font-size:8.5px;line-height:12px;letter-spacing:-.2px}
.apply .btns{margin-top:12px;display:flex;align-items:center;gap:5px;font-size:7.5px}
.apply .btn{background:var(--cyan);padding:2px 4px;font-size:9.5px}

/* services */
.card{top:407px;width:193px}
.card .img{height:96px}
.card h2{font-family:"Varela Round",sans-serif;font-weight:400;font-size:21px;color:var(--slate);margin-top:16px;letter-spacing:-.3px;white-space:nowrap}
.card ul{list-style:none;font-size:9.5px;color:var(--muted);line-height:12px;margin-top:7px;height:36px}
.card .more{font-size:9.5px;color:var(--cyan);margin-top:12px}
.card .bar{height:5px;background:var(--rule);margin-top:11px}
.card .bar.on{background:var(--cyan)}

/* welcome */
.welcome{left:201px;top:653px;width:780px}
.welcome h1{font-family:"Varela Round",sans-serif;font-weight:400;font-size:13.5px;color:var(--slate);margin-bottom:3px}
.welcome p{font-size:9px;line-height:15.2px;color:#a0a3ab}

/* footer */
.footer{left:0;top:756px;width:1200px;height:98px;background:var(--page-grey)}
.share{left:203px;top:769px;display:flex;flex-direction:column;gap:10px}
.share span{display:inline-block;width:fit-content;background:#f4f6f9;border:1px solid #c3c9d3;color:#3b5a8a;font-size:8px;padding:2px 4px}
.foot-col{top:769px;list-style:none;font-size:8.5px;color:var(--slate);line-height:14.4px;letter-spacing:.3px}
.social li{display:flex;align-items:center;gap:7px}
.social i{width:10px;height:10px;border-radius:2px;display:inline-block}
.news{left:0;top:858px;width:1200px;height:45px;background:var(--slate)}
.news-row{left:199px;top:865px;display:flex;align-items:center;gap:4px;color:var(--white);font-size:9.5px;font-weight:700;letter-spacing:.4px}
.news-row .email{width:166px;height:17px;background:var(--white);border:1px solid #b9bbc2;color:#9a9ca5;font-size:8px;font-weight:400;padding:4px 5px;margin-right:8px;letter-spacing:0}
.news-row .join{background:var(--cyan);font-family:"Varela Round",sans-serif;font-weight:400;font-size:11px;padding:2px 7px}
</style>
</head>
<body>

<header>
  <div class="abs header-band"></div>
  <div class="abs account-links"><span>My Account ›</span><span>Login ›</span><span>Register ›</span></div>
  <div class="abs logo"><span class="logo-mark"></span><span class="logo-name">Corvella Lending</span></div>
  <div class="abs advice">
    <svg width="18" height="24" viewBox="0 0 18 24"><path d="M4 1 L8 2 L8 8 L5 9 C5 13 7 16 10 18 L12 15 L17 17 L16 22 C8 23 1 15 1 5 Z" fill="#3a3d4a"/></svg>
    <small>for advice call:</small>
    <strong>1800 552 418</strong>
  </div>
  <div class="abs util-links">ABOUT US &nbsp;| FAQ &nbsp;| CONTACT US</div>
</header>

<nav>
  <div class="abs nav-band"></div>
  <div class="abs main-nav">
    <a class="nav-services" href="#">Services</a><a class="nav-home" href="#">Home loans</a><a class="nav-invest" href="#">Investment loans</a><a class="nav-refi" href="#">Refinancing loans</a><a class="nav-business" href="#">Business loans</a>
  </div>
  <div class="abs search">Type search here...
    <svg width="12" height="12" viewBox="0 0 12 12"><circle cx="7" cy="5" r="3.5" fill="none" stroke="#333" stroke-width="1.5"/><line x1="4.5" y1="7.5" x2="1" y2="11" stroke="#333" stroke-width="1.8"/></svg>
  </div>
</nav>

<section>
  <div class="abs hero-band"></div>
  <div class="abs hero" role="img" aria-label="Photo of a smiling family playing outdoors in a sunny park"></div>
  <div class="abs hero-title">morgage loans</div>
  <div class="abs hero-link">Click here ›</div>
  <div class="abs dots"><i class="on"></i><i></i><i></i><i></i></div>

  <div class="abs calc"></div>
  <div class="abs calc-head">Loan calculator</div>
  <div class="abs calc-row" style="left:768px;top:126px">I would like to borrow <span class="field" style="margin-left:2px">£10,000</span></div>
  <div class="abs calc-row" style="left:768px;top:150px">£1,000</div>
  <div class="abs calc-row" style="left:954px;top:150px">£25,000</div>
  <div class="abs track" style="left:768px;top:163px;width:227px"><div class="fill" style="width:114px"></div><div class="abs knob" style="left:106px"></div></div>
  <div class="abs ticks" style="left:769px;top:172px;width:225px"><span style="width:48px">19.9%</span><span class="blank" style="width:48px">6.8%</span><span style="width:103px;margin-left:24px">15.4%</span></div>
  <div class="abs" style="left:762px;top:192px;width:238px;height:1px;background:#dcdde0"></div>
  <div class="abs calc-row" style="left:768px;top:199px">And pay it back over <span class="field">36</span> month</div>
  <div class="abs calc-row" style="left:768px;top:221px">12 month</div>
  <div class="abs calc-row" style="left:945px;top:221px">84 month</div>
  <div class="abs track" style="left:768px;top:234px;width:227px"><div class="fill" style="width:114px"></div><div class="abs knob" style="left:106px"></div></div>
  <div class="abs ticks" style="left:769px;top:243px;width:225px"><span style="flex:1">1yr</span><span style="flex:1">2yr</span><span style="flex:1">3yr</span><span style="flex:1">4yr</span><span style="flex:1">5yr</span><span style="flex:1">6yr</span></div>

  <div class="abs repay">
    <h3>Repayments</h3>
    <p>Monthly repayments<b>£307.13</b></p>
    <p>Total repayable<b>£11,056.68</b></p>
    <p>Representative APR<b>6.8%</b></p>
  </div>
  <div class="abs apply">
    <h3>Apply</h3>
    <ul><li>From £1,000 to £25,000</li><li>Overpay</li><li>Over 1 to 7 years</li><li>Fixed repayments</li><li>Quick, easy and secure</li></ul>
    <div class="btns"><span class="btn">apply</span><span>more info ›</span></div>
  </div>
</section>

<section>
  <div class="abs card" style="left:199px">
    <div class="img" role="img" aria-label="Photo of a hand holding a small model house" style="background:linear-gradient(90deg,#d9d5cf,#a48a72 40%,#4b4e52 60%,#e6e3df)"></div>
    <h2>Home Loan</h2>
    <ul><li>Home buyers</li><li>First home buyers</li><li>Over 20 lenders</li></ul>
    <div class="more">View more ›</div><div class="bar on"></div>
  </div>
  <div class="abs card" style="left:402px">
    <div class="img" role="img" aria-label="Photo of two business people shaking hands" style="background:linear-gradient(110deg,#3a3c40,#6b6d72 35%,#c9a58c 55%,#e9e9ea)"></div>
    <h2>Investment loan</h2>
    <ul><li>Property investment loans</li><li>Interest only loans</li></ul>
    <div class="more">View more ›</div><div class="bar"></div>
  </div>
  <div class="abs card" style="left:606px">
    <div class="img" role="img" aria-label="Photo of a stack of silver coins" style="background:radial-gradient(ellipse at 55% 55%,#6f6d68 0%,#a9a7a2 30%,#eeeeed 65%)"></div>
    <h2>Refinancing</h2>
    <ul><li>Refinancing for the best rate</li><li>Upsizing or downsizing</li><li>Change from a variable to a fixed rate</li></ul>
    <div class="more">View more ›</div><div class="bar"></div>
  </div>
  <div class="abs card" style="left:808px">
    <div class="img" role="img" aria-label="Photo of a pen beside an approved stamp on paper" style="background:linear-gradient(160deg,#dcdcde,#f3f3f4 40%,#d6d6d8)"></div>
    <h2>Business loan</h2>
    <ul><li>Long term</li><li>Short term</li><li>Equipment and Leasing</li></ul>
    <div class="more">View more ›</div><div class="bar"></div>
  </div>
</section>

<section class="abs welcome">
  <h1>Welcome to Corvella Lending</h1>
  <p>At Corvella Lending we work hard to find the right loan for our customers. We do that because we are backed by sound industry knowledge, professional experience and a great customer service approach. Corvella Lending guarantees that we will always tailor the best solution for your individual lending needs. We can do that because we have access to a wide variety of lending options from major banks to non-bank lenders and we are committed to finding the right lending product for you.</p>
</section>

<footer>
  <div class="abs footer"></div>
  <div class="abs share"><span>Like</span><span>Post</span><span>+1</span></div>
  <ul class="abs foot-col social" style="left:303px">
    <li><i style="background:#3b5a9a"></i>Join us on Friendlio</li>
    <li><i style="background:#5cc2ee"></i>Follow us on Chirper</li>
    <li><i style="background:#f28a22"></i>RSS Feeds</li>
    <li><i style="background:#ef6a22"></i>Bookmark</li>
  </ul>
  <ul class="abs foot-col" style="left:507px"><li>• About Us</li><li>• Contact Us</li><li>• FAQs</li></ul>
  <ul class="abs foot-col" style="left:675px"><li>• Recruitment</li><li>• Blog</li><li>• Site Map</li></ul>
  <ul class="abs foot-col" style="left:848px"><li>• Legal Information</li><li>• Privacy Policy</li><li>• Terms &amp; Conditions</li></ul>

  <div class="abs news"></div>
  <div class="abs news-row">
    <svg width="15" height="10" viewBox="0 0 15 10"><rect x="0.5" y="0.5" width="14" height="9" fill="#d9dbe0" stroke="#aeb1b9"/><path d="M0.5 0.5 L7.5 6 L14.5 0.5" fill="none" stroke="#8c8f99"/></svg>
    <span>JOIN OUR NEWSLETTER:</span>
    <span class="email">Your Email...</span>
    <span class="join">join</span>
  </div>
</footer>

</body>
</html>
```